Business Card for Yachting Management Company

Need a business card design for a new yachting project management company. Attached is the logo for the company.
Our clients are large yacht owners and captains.
Design must be in the style of the logo. Modern, elegant.

Example of data to show:
Oliver Tennant
Project Manager
(+34) 612 870 334
oliver@quarvel.net
Quarvel Management - Marisol Tower, Office 22 - NDR - Palma de Mallorca

The data above will have to be changed (by me) for the different people in the company over the next years.

Will be printed using CardHarbor (Lustrel Business Cards). They provide these guidelines for the size:
"the actual size of the card is 1050 x 600 pixels. However, the full bleed size is 1083 x 633 pixels, and the safe printing area is 1008 x 558 pixels."

```html
<!DOCTYPE html>
<html lang="en">
<head>
<meta charset="utf-8">
<title>Quarvel Management – Business Card</title>
<link rel="stylesheet" href="https://fonts.googleapis.com/css2?family=Montserrat:wght@400;500;600&display=swap">
<style>
  :root {
    --page-bg: #1a1a1a;
    --card-bg: #222222;
    --card-bg-light: #2b2b2b;
    --silver: #d4d4d4;
    --silver-soft: #b9b9b9;
    --rule: #8a8a8a;
    --accent-blue: #1f7fd1;
  }
  * { box-sizing: border-box; margin: 0; padding: 0; }
  html, body {
    width: 1200px; height: 900px; overflow: hidden;
    background: var(--page-bg);
    font-family: "Montserrat", sans-serif;
  }
  .canvas {
    position: relative; width: 1200px; height: 900px;
  }
  .card {
    position: absolute; left: 250px; width: 700px; height: 400px;
    background: linear-gradient(135deg, var(--card-bg) 0%, var(--card-bg-light) 70%, var(--card-bg) 100%);
    box-shadow: 0 10px 30px rgba(0,0,0,.6);
  }
  .card--front { top: 30px; }
  .card--back { top: 470px; }

  .wordmark {
    display: flex; align-items: center; gap: 12px;
    color: var(--silver); font-weight: 600; letter-spacing: 2px;
    text-transform: uppercase; white-space: nowrap;
  }
  .wordmark__square { width: 14px; height: 14px; background: var(--silver); }
  .card--front .wordmark {
    position: absolute; left: 50%; top: 50%; transform: translate(-50%, -50%);
    font-size: 30px;
  }
  .card--back .wordmark {
    position: absolute; right: 40px; top: 60px; font-size: 20px;
  }

  .accent-bar {
    position: absolute; left: 0; top: 152px; width: 9px; height: 40px;
    background: var(--accent-blue);
  }
  .person { position: absolute; left: 36px; top: 150px; }
  .person__name {
    color: var(--silver); font-size: 24px; font-weight: 600; letter-spacing: 1.5px;
  }
  .person__title { color: var(--silver-soft); font-size: 14px; margin-top: 2px; }

  .divider {
    position: absolute; left: 36px; top: 210px; width: 500px; height: 1px;
    background: linear-gradient(90deg, var(--rule), var(--silver) 70%, rgba(200,200,200,0));
  }

  .contact { position: absolute; left: 22px; top: 226px; list-style: none; }
  .contact li {
    display: flex; align-items: center; gap: 6px;
    color: var(--silver); font-size: 15px; line-height: 23px;
  }
  .contact svg { width: 11px; height: 11px; fill: none; stroke: var(--silver); stroke-width: 1.6; }

  .address {
    position: absolute; right: 40px; bottom: 34px; text-align: right;
    color: var(--silver); font-size: 15px; line-height: 21px;
  }
  .address__rule {
    width: 190px; height: 1px; background: var(--rule); margin: 0 0 8px auto;
  }
</style>
</head>
<body>
<main class="canvas">
  <section class="card card--front" aria-label="Card front">
    <div class="wordmark"><span class="wordmark__square"></span>Quarvel Management</div>
  </section>

  <section class="card card--back" aria-label="Card back">
    <div class="wordmark"><span class="wordmark__square"></span>Quarvel Management</div>

    <span class="accent-bar"></span>
    <div class="person">
      <p class="person__name">OLIVER TENNANT</p>
      <p class="person__title">Project Manager</p>
    </div>
    <div class="divider"></div>

    <ul class="contact">
      <li>
        <svg viewBox="0 0 12 12"><path d="M3 1l2 2.5-1.2 1.3c.6 1.3 1.6 2.3 2.9 2.9L8 6.5 10.5 8.5 9.5 11C5 10.5 1.5 7 1 2.5z"/></svg>
        (+34) 612 870 334
      </li>
      <li>
        <svg viewBox="0 0 12 12"><rect x="1" y="2.5" width="10" height="7"/><path d="M1 2.5l5 4 5-4"/></svg>
        oliver@quarvel.net
      </li>
      <li>
        <svg viewBox="0 0 12 12"><circle cx="6" cy="6" r="5"/><ellipse cx="6" cy="6" rx="2.2" ry="5"/><path d="M1 6h10"/></svg>
        www.quarvelmanagement.net
      </li>
    </ul>

    <div class="address">
      <div class="address__rule"></div>
      <p>Quarvel Management</p>
      <p>Marisol Tower, Office 22</p>
      <p>NDR - Palma de Mallorca</p>
    </div>
  </section>
</main>
</body>
</html>
```